Business card design for Medical Practice Mgmt company
Ashfield Clinic Allies
Business card design for Medical Practice Mgmt company - Medical
Creative Brief
Professional
Monica Daltrey
VP of Operations
4170 E Holloway Ln # 210 Plano, TX 75041
mdaltrey@aca-mail.net
www.ashfieldclinicallies.net
jdovan jdovan
uploaded AI file
bluefern bluefern
Logo Ai file needed!

```html
<!DOCTYPE html>
<html lang="en">
<head>
<meta charset="utf-8">
<title>Ashfield Clinic Allies – Business Cards</title>
<link rel="stylesheet" href="https://fonts.googleapis.com/css2?family=Montserrat:wght@300;400;600&display=swap">
<style>
  :root {
    --page-bg: #e9eaec;
    --card-white: #ffffff;
    --card-black: #0b0b0c;
    --brand-blue: #2a7fc1;
    --brand-blue-light: #8cc1e8;
    --ink: #2b2b2d;
    --ink-soft: #5c5f63;
    --back-text: #d9dadc;
    --shadow: rgba(0, 0, 0, 0.28);
  }
  * { margin: 0; padding: 0; box-sizing: border-box; }
  html, body { width: 1200px; height: 1005px; overflow: hidden; }
  body {
    background: var(--page-bg);
    font-family: "Montserrat", Arial, sans-serif;
    color: var(--ink);
    position: relative;
  }
  .card {
    position: absolute;
    width: 620px;
    height: 354px;
    border-radius: 22px;
    overflow: hidden;
    box-shadow: 0 14px 30px var(--shadow);
  }

  /* Back of card */
  .card-back {
    left: 520px;
    top: 90px;
    background: var(--card-black);
  }
  .back-mark {
    position: absolute;
    left: 0; right: 0;
    top: 120px;
    display: flex;
    align-items: center;
    justify-content: center;
    gap: 14px;
  }
  .back-mark .mark-dot {
    width: 34px; height: 34px;
    border-radius: 50%;
    background: var(--brand-blue);
  }
  .back-mark .mark-name {
    font-size: 26px;
    font-weight: 400;
    color: var(--back-text);
  }
  .back-web {
    position: absolute;
    left: 64px;
    bottom: 62px;
    font-size: 15px;
    letter-spacing: 4px;
    color: var(--back-text);
    font-weight: 400;
  }

  /* Front of card */
  .card-front {
    left: 60px;
    top: 560px;
    background: var(--card-white);
  }
  .front-logo {
    position: absolute;
    left: 150px;
    top: 34px;
    display: flex;
    align-items: center;
    gap: 12px;
  }
  .front-logo .mark-dot {
    width: 30px; height: 30px;
    border-radius: 50%;
    background: var(--brand-blue);
  }
  .front-logo .mark-name {
    font-size: 30px;
    font-weight: 400;
    color: var(--ink);
  }
  .front-tagline {
    position: absolute;
    left: 192px;
    top: 78px;
    font-size: 10px;
    letter-spacing: 1.5px;
    color: var(--ink-soft);
    text-transform: uppercase;
  }
  .person {
    position: absolute;
    left: 150px;
    top: 120px;
    width: 200px;
    text-align: right;
    padding-right: 16px;
    border-right: 1px solid var(--brand-blue-light);
  }
  .person-name { font-size: 14px; font-weight: 600; color: var(--brand-blue); }
  .person-title { font-size: 10px; color: var(--ink-soft); margin-bottom: 8px; }
  .person-address { font-size: 10px; line-height: 1.5; color: var(--ink-soft); }
  .contact-list {
    position: absolute;
    left: 368px;
    top: 120px;
    list-style: none;
    font-size: 10px;
    color: var(--ink-soft);
  }
  .contact-list li {
    display: flex;
    align-items: center;
    gap: 7px;
    height: 17px;
  }
  .contact-icon {
    width: 11px; height: 11px;
    border-radius: 50%;
    background: var(--brand-blue);
    flex: none;
  }
  .card-wave {
    position: absolute;
    left: 0; top: 0;
    width: 620px; height: 354px;
  }
</style>
</head>
<body>

  <section class="card card-back" aria-label="Card back">
    <div class="back-mark">
      <span class="mark-dot"></span>
      <span class="mark-name">Ashfield Clinic Allies</span>
    </div>
    <p class="back-web">www.ashfieldclinicallies.net</p>
  </section>

  <section class="card card-front" aria-label="Card front">
    <svg class="card-wave" viewBox="0 0 620 354" aria-hidden="true">
      <path d="M0 270 C160 210 340 300 620 236 L620 250 C340 314 160 224 0 284 Z" fill="var(--brand-blue-light)"/>
      <path d="M0 282 C160 222 340 312 620 248 L620 266 C340 330 160 240 0 300 Z" fill="var(--brand-blue)"/>
      <path d="M0 300 C160 240 340 330 620 266 L620 354 L0 354 Z" fill="var(--card-black)"/>
    </svg>

    <div class="front-logo">
      <span class="mark-dot"></span>
      <span class="mark-name">Ashfield Clinic Allies</span>
    </div>
    <p class="front-tagline">Practice Management Services</p>

    <div class="person">
      <p class="person-name">Monica Daltrey</p>
      <p class="person-title">VP of Operations</p>
      <p class="person-address">4170 E Holloway Ln<br># 210 Plano, TX 75041</p>
    </div>

    <ul class="contact-list">
      <li><span class="contact-icon"></span>469-555-0142</li>
      <li><span class="contact-icon"></span>469-555-0187</li>
      <li><span class="contact-icon"></span>469-555-0163</li>
      <li><span class="contact-icon"></span>mdaltrey@aca-mail.net</li>
      <li><span class="contact-icon"></span>www.ashfieldclinicallies.net</li>
    </ul>
  </section>

</body>
</html>
```